Growth-Bridge: Plus - EU-funded management consulting

A website to inform possible customers about my management consulting services for small and medium sized companies. I am using a funding for small and medium companies to do 10 days of workshops and coaching about leadership, further education and employee's health. The Funding is called "Wachstumsbrücke Plus" which means something like: Humans are the value of the company. The official logo is attached as a

Target Market(s)

Small and medium sized companies that want to improve their employee's well being and efficiency.

Industry/Entity Type

Management Consulting

Contact Information for Business Card

Veit Brosche, Kastanienweg 14, 10437 Berlin

Logo Text

WachstumsBrücke Plus - Beratung

Font styles to use
Serif
Sans Serif

Requirements
Must have
• a friendly and professional design
Nice to have
• saying somthing about: employees, leadership, further education and employees health are important to us.
Should not have
• should not be too shimmering

```html
<!DOCTYPE html>
<html lang="en">
<head>
<meta charset="utf-8">
<title>WachstumsBrücke Plus – Beratung</title>
<link href="https://fonts.googleapis.com/css2?family=Oswald:wght@400;500&family=Open+Sans:wght@400;600;700&family=Merriweather:wght@400&display=swap" rel="stylesheet">
<style>
:root{
  --navy:#0b2470;
  --blue:#1a47a8;
  --blue-light:#2d63c8;
  --red:#c4161c;
  --ink:#1c2b4a;
  --text:#6b6f78;
  --line:#e3e6ec;
  --white:#ffffff;
  --footer:#0a1c4e;
  --footer-dark:#07133a;
}
*{box-sizing:border-box;margin:0;padding:0}
html,body{width:719px;height:1200px;overflow:hidden;background:var(--white)}
body{font-family:"Open Sans",Arial,sans-serif;color:var(--text);position:relative}
.container{width:650px;margin:0 auto;position:relative}

/* header */
.site-header{height:44px;background:var(--white);position:relative;z-index:2;box-shadow:0 1px 3px rgba(0,0,0,.15)}
.site-header .container{display:flex;align-items:center;justify-content:space-between;height:44px}
.brand{display:flex;align-items:center;gap:6px;font-family:"Open Sans",sans-serif;font-weight:700;font-size:11px;color:var(--navy);line-height:1.1}
.brand-mark{width:14px;height:14px;background:var(--blue)}
.main-nav{display:flex;gap:2px}
.main-nav a{font-family:"Oswald",sans-serif;font-size:8px;letter-spacing:.5px;color:var(--ink);text-decoration:none;padding:7px 8px}
.main-nav a.active{background:var(--red);color:var(--white)}

/* hero */
.hero-band{height:356px;background:linear-gradient(180deg,var(--navy) 0%,var(--blue) 70%,#3c6bc4 100%);padding-top:11px}
.hero-slide{height:335px;position:relative;background:linear-gradient(135deg,#dfe6ee 0%,#c7d3df 45%,#8a97a8 100%)}
.hero-caption{position:absolute;left:22px;top:150px;background:var(--navy);color:var(--white);font-family:"Merriweather",serif;font-size:15px;line-height:1.35;padding:7px 12px;text-transform:uppercase;letter-spacing:.3px}
.slider-dots{position:absolute;bottom:8px;left:50%;transform:translateX(-50%);display:flex;gap:4px}
.slider-dots span{width:5px;height:5px;border-radius:50%;background:rgba(255,255,255,.6)}
.slider-dots span.on{background:var(--white)}

/* welcome */
.welcome{height:168px;padding-top:12px}
.welcome .container{height:100%}
.section-title{font-family:"Oswald",sans-serif;font-weight:400;font-size:16px;color:var(--ink);letter-spacing:.3px}
.welcome-text{width:505px;font-size:8px;line-height:12.5px;margin-top:6px}
.welcome-portrait{position:absolute;right:6px;top:0;width:88px;height:136px;background:linear-gradient(180deg,#e9edf2 0%,#2c3548 60%,#1b2233 100%)}
.welcome-bar{position:absolute;left:0;top:116px;display:flex;align-items:center;gap:10px}
.btn-more{background:var(--navy);color:var(--white);font-size:7px;font-weight:700;padding:5px 12px;letter-spacing:.4px}
.values{display:flex;gap:10px;font-family:"Oswald",sans-serif;font-size:11px;color:var(--ink)}
.values span{display:flex;align-items:center;gap:4px}
.values svg{width:9px;height:9px}

/* services */
.services{height:140px;border-top:1px solid var(--line)}
.services .container{display:flex;height:100%;padding-top:14px}
.service{flex:1;text-align:center;padding:0 14px;border-left:1px solid var(--line)}
.service:first-child{border-left:0}
.service svg{width:30px;height:30px;display:block;margin:0 auto 6px}
.service h3{font-family:"Oswald",sans-serif;font-weight:400;font-size:11px;color:var(--ink);letter-spacing:.4px;margin-bottom:5px}
.service p{font-size:7px;line-height:10.5px}

/* news */
.news{height:180px;background:linear-gradient(180deg,var(--blue) 0%,var(--navy) 100%);padding-top:12px}
.news .section-title{color:var(--white);font-size:14px;margin-bottom:9px}
.news-grid{display:flex;gap:10px}
.news-card{flex:1;color:var(--white)}
.news-thumb{height:82px;background:linear-gradient(135deg,#d9e2ec,#9fb0c4)}
.news-thumb.t2{background:linear-gradient(135deg,#e4e9ef,#a9b8c9)}
.news-thumb.t3{background:linear-gradient(135deg,#cfdce9,#8ea3bb)}
.news-thumb.t4{background:linear-gradient(135deg,#e8edf2,#b4c2d1)}
.news-date{font-weight:700;font-size:8px;margin-top:6px}
.news-card p{font-size:7px;line-height:10px;opacity:.85;margin-top:2px}

/* partners */
.partners{height:66px;display:flex;align-items:center}
.partners .container{display:flex;justify-content:space-between;align-items:center}
.partner{height:14px;background:#c7cbd3;border-radius:2px}

/* footer */
.site-footer{height:222px;background:var(--footer);color:#c3cbe0;padding-top:16px}
.footer-grid{display:flex;gap:18px}
.footer-col h4{font-family:"Oswald",sans-serif;font-weight:400;font-size:10px;color:var(--white);letter-spacing:.5px;padding-bottom:5px;border-bottom:1px solid rgba(255,255,255,.2);margin-bottom:7px}
.col-links{width:128px}
.col-news{width:140px}
.col-contact{width:160px}
.col-map{flex:1}
.link-list{display:grid;grid-template-columns:1fr 1fr;gap:5px 6px;font-size:7px;list-style:none}
.link-list li::before{content:"› ";color:var(--red)}
.col-news p{font-size:7px;line-height:10px;margin-bottom:8px}
.field{height:18px;background:var(--white);font-size:7px;color:#999;padding:4px 6px;margin-bottom:6px}
.btn-subscribe{display:inline-block;background:var(--red);color:var(--white);font-size:7px;font-weight:700;padding:5px 14px;letter-spacing:.4px}
.contact-row{display:flex;gap:6px;font-size:7px;line-height:10px;margin-bottom:7px}
.contact-row svg{width:9px;height:9px;flex:none;margin-top:1px}
.contact-row strong{color:var(--white);font-weight:600}
.map-box{height:96px;background:linear-gradient(135deg,#e7eadf,#cdd8c4)}
.footer-bottom{position:absolute;left:0;right:0;bottom:0;height:28px;background:var(--footer-dark);font-size:7px;color:#8e98b5}
.footer-bottom .container{display:flex;justify-content:space-between;align-items:center;height:28px}
.social{display:flex;gap:3px}
.social span{width:11px;height:11px;background:var(--blue-light)}
</style>
</head>
<body>

<header class="site-header">
  <div class="container">
    <div class="brand"><span class="brand-mark"></span><span>WACHSTUMSBRÜCKE PLUS</span></div>
    <nav class="main-nav">
      <a class="active">HOME</a><a>ABOUT</a><a>SERVICES</a><a>PROJECTS</a><a>OUR BLOG</a><a>CONTACT US</a>
    </nav>
  </div>
</header>

<section class="hero-band">
  <div class="container hero-slide" role="img" aria-label="Photo of a smiling consultant in a suit in a bright office with colleagues in the background">
    <div class="hero-caption">Conduct workshops on<br>leadership</div>
    <div class="slider-dots"><span class="on"></span><span></span><span></span><span></span></div>
  </div>
</section>

<section class="welcome">
  <div class="container">
    <h2 class="section-title">WELCOME TO WACHSTUMSBRÜCKE PLUS</h2>
    <p class="welcome-text">We support small and medium sized companies in growing with their people. Our funded programme combines ten days of workshops and coaching on leadership, further education and employee health. Together we analyse your current situation, define clear goals and develop practical measures that fit your daily work. Every step is tailored to your team, your sector and your resources. The programme is co-financed, so the investment for your company stays low while the benefits for your staff and your results remain lasting.</p>
    <div class="welcome-portrait" role="img" aria-label="Portrait photo of a consultant in a dark suit"></div>
    <div class="welcome-bar">
      <span class="btn-more">READ MORE ›</span>
      <div class="values">
        <span><svg viewBox="0 0 10 10"><path d="M1 5l3 3 5-6" fill="none" stroke="#c4161c" stroke-width="2"/></svg>American Success</span>
        <span><svg viewBox="0 0 10 10"><path d="M5 0l5 5-5 5-5-5z" fill="#c4161c"/></svg>Business</span>
        <span><svg viewBox="0 0 10 10"><path d="M5 9L1 5a2.2 2.2 0 0 1 4-3 2.2 2.2 0 0 1 4 3z" fill="#c4161c"/></svg>We care for our employes</span>
      </div>
    </div>
  </div>
</section>

<section class="services">
  <div class="container">
    <div class="service">
      <svg viewBox="0 0 30 30" fill="none" stroke="#c4161c" stroke-width="2"><rect x="4" y="6" width="22" height="14" rx="1"/><path d="M10 25h10M15 20v5"/></svg>
      <h3>WORKSHOPS</h3>
      <p>Practical sessions that strengthen leadership skills and help teams work together with clarity.</p>
    </div>
    <div class="service">
      <svg viewBox="0 0 30 30" fill="none" stroke="#c4161c" stroke-width="2"><rect x="4" y="8" width="22" height="16" rx="2"/><path d="M11 8V5h8v3M15 12v8M11 16h8"/></svg>
      <h3>EMPLOYEES HEALTH</h3>
      <p>Measures for healthy workplaces that reduce stress and keep your people motivated and fit.</p>
    </div>
    <div class="service">
      <svg viewBox="0 0 30 30" fill="none" stroke="#c4161c" stroke-width="2"><path d="M3 7c4-2 8-2 12 1 4-3 8-3 12-1v17c-4-2-8-2-12 1-4-3-8-3-12-1z"/><path d="M15 8v17"/></svg>
      <h3>EDUCATION</h3>
      <p>Further education plans that build the skills your company needs for tomorrow's tasks.</p>
    </div>
    <div class="service">
      <svg viewBox="0 0 30 30" fill="none" stroke="#c4161c" stroke-width="2"><path d="M6 17v-3a9 9 0 0 1 18 0v3"/><rect x="4" y="16" width="5" height="8" rx="1"/><rect x="21" y="16" width="5" height="8" rx="1"/></svg>
      <h3>SUPPORT</h3>
      <p>Personal coaching and guidance from the first analysis to the final results report.</p>
    </div>
  </div>
</section>

<section class="news">
  <div class="container">
    <h2 class="section-title">LATEST NEWS</h2>
    <div class="news-grid">
      <article class="news-card"><div class="news-thumb" role="img" aria-label="Photo of a team meeting at a table"></div><div class="news-date">08 AUG, 2015</div><p>New funding round opens for small companies in Berlin</p></article>
      <article class="news-card"><div class="news-thumb t2" role="img" aria-label="Photo of colleagues working at laptops"></div><div class="news-date">10 AUG, 2015</div><p>Leadership workshop series starts with twelve local firms</p></article>
      <article class="news-card"><div class="news-thumb t3" role="img" aria-label="Photo of a group discussion in an office"></div><div class="news-date">14 AUG, 2015</div><p>Five simple steps towards healthier daily work</p></article>
      <article class="news-card"><div class="news-thumb t4" role="img" aria-label="Photo of a coaching session with a presenter"></div><div class="news-date">17 AUG, 2015</div><p>Coaching results presented at the regional business forum</p></article>
    </div>
  </div>
</section>

<section class="partners">
  <div class="container">
    <span class="partner" style="width:56px"></span>
    <span class="partner" style="width:40px"></span>
    <span class="partner" style="width:44px"></span>
    <span class="partner" style="width:52px"></span>
    <span class="partner" style="width:40px"></span>
    <span class="partner" style="width:58px"></span>
    <span class="partner" style="width:36px"></span>
  </div>
</section>

<footer class="site-footer">
  <div class="container footer-grid">
    <div class="footer-col col-links">
      <h4>QUICK LINKS</h4>
      <ul class="link-list">
        <li>Home</li><li>Partners</li>
        <li>About Us</li><li>Privacy Policy</li>
        <li>Services</li><li>Imprint</li>
        <li>Our Blog</li><li>Sitemap</li>
        <li>Projects</li><li>FAQ</li>
        <li>Contact Us</li><li>Terms</li>
      </ul>
    </div>
    <div class="footer-col col-news">
      <h4>NEWSLETTER</h4>
      <p>Sign up to receive news about workshops and funding.</p>
      <div class="field">Email Address</div>
      <span class="btn-subscribe">SUBSCRIBE</span>
    </div>
    <div class="footer-col col-contact">
      <h4>CONTACT US</h4>
      <div class="contact-row"><svg viewBox="0 0 10 10"><path d="M5 10S1.5 6 1.5 4a3.5 3.5 0 0 1 7 0C8.5 6 5 10 5 10z" fill="#c4161c"/><circle cx="5" cy="4" r="1.2" fill="#0a1c4e"/></svg><span><strong>WACHSTUMSBRÜCKE PLUS</strong><br>Veit Brosche<br>Kastanienweg 14, 10437 Berlin</span></div>
      <div class="contact-row"><svg viewBox="0 0 10 10"><path d="M2 1h2l1 2.5-1.3 1a5 5 0 0 0 1.8 1.8l1-1.3L9 6v2a1 1 0 0 1-1 1A7 7 0 0 1 1 2a1 1 0 0 1 1-1z" fill="#c4161c"/></svg><span>+49 30 5550 1847</span></div>
      <div class="contact-row"><svg viewBox="0 0 10 10"><rect x=".5" y="2" width="9" height="6" fill="#c4161c"/><path d="M.5 2L5 5.5 9.5 2" fill="none" stroke="#0a1c4e" stroke-width=".8"/></svg><span>info@wachstumsbruecke-plus.de</span></div>
    </div>
    <div class="footer-col col-map">
      <h4>OUR LOCATION</h4>
      <div class="map-box" role="img" aria-label="Street map showing the office location in Berlin"></div>
    </div>
  </div>
  <div class="footer-bottom">
    <div class="container">
      <span>© 2015 Wachstumsbrücke Plus. All rights reserved.</span>
      <div class="social"><span></span><span></span><span></span><span></span></div>
    </div>
  </div>
</footer>

</body>
</html>
```